This book will apply the 12 Steps to gaming addiction, also known as video game addiction. The primary purpose of the book is to provide an effective solution for this new type of addiction. The solution is based on the rich and successful concepts of traditional twelve-step programs like RL.

The title on the cover will be "Nine Doors Past the Glowing Screen" and "by Martin Quorby". A subtitle can be used if it works in your design of "A Practical Path Beyond Compulsive Console Play". Cover will be for a 6" x 9" book approximately 110 pages in length.

Some back cover text including some review quotes and an author bio are in the attached Word doc. There is also an author photo attached for for the back cover.

Requirements
Must have
• For the cover design it could be stylized, or an image, a partial image, or whatever. I am open to suggestions. Think about what would be noticed by a person searching for help with moderating their video game use, or by the parents or loved ones of problem gamers. Something contemporary and eye catching.

```html
<!DOCTYPE html>
<html lang="en">
<head>
<meta charset="utf-8">
<title>Nine Doors Past the Glowing Screen – Cover Spread</title>
<link rel="stylesheet" href="https://fonts.googleapis.com/css2?family=Poppins:wght@400;600;700&family=Saira+Condensed:wght@500;600;700&family=Saira:wght@600;700&display=swap">
<style>
  :root {
    --page: #ffffff;
    --ink: #05070c;
    --white: #f4f6fa;
    --orange: #ff8a4c;
    --orange-light: #ffb27a;
    --violet: #9a7bff;
    --pink: #ff5fa8;
    --blue: #5aa0ff;
    --steel: #7f9fd6;
    --gold: #f4b63a;
    --line: #7f9fd6;
  }
  * { margin: 0; padding: 0; box-sizing: border-box; }
  html, body { width: 1200px; height: 1000px; overflow: hidden; background: var(--page); }
  .spread {
    position: absolute; left: 20px; top: 30px; width: 1165px; height: 792px;
    background: var(--ink); overflow: hidden;
    font-family: "Poppins", sans-serif; color: var(--white);
  }
  /* back cover */
  .back {
    position: absolute; left: 0; top: 0; width: 548px; height: 100%;
    background: linear-gradient(180deg, #050810 0%, #08111d 55%, #050810 100%);
  }
  .back__heading {
    position: absolute; left: 60px; top: 28px;
    font-family: "Saira Condensed", sans-serif; font-weight: 600; font-size: 19px;
    letter-spacing: 0.5px; text-transform: uppercase; color: var(--white);
  }
  .back__heading span {
    background: linear-gradient(90deg, var(--orange), var(--pink), var(--violet));
    -webkit-background-clip: text; background-clip: text; color: transparent;
  }
  .praise { position: absolute; left: 60px; width: 420px; font-size: 9.6px; line-height: 1.32; font-weight: 600; text-align: justify; }
  .praise__name { display: block; text-align: left; font-weight: 600; color: var(--white); }
  .praise__name b { color: var(--steel); font-weight: 700; }
  .praise--one { top: 68px; }
  .praise--two { top: 170px; }
  .praise--three { top: 218px; }
  .divider { position: absolute; left: 60px; top: 306px; width: 420px; height: 1px; background: rgba(127,159,214,0.45); }
  .blurb { position: absolute; left: 60px; top: 320px; width: 420px; font-size: 9.6px; line-height: 1.34; font-weight: 600; text-align: justify; }
  .blurb p { margin-bottom: 11px; }
  .bio-band {
    position: absolute; left: 0; top: 540px; width: 548px; height: 126px;
    background: linear-gradient(90deg, rgba(14,42,79,0.9), rgba(14,42,79,0.55) 70%, rgba(14,42,79,0.15));
  }
  .bio-photo {
    position: absolute; left: 58px; top: 554px; width: 74px; height: 86px;
    background: linear-gradient(180deg, #c9d3de 0%, #8a93a0 60%, #2a2f3a 100%);
  }
  .bio-text { position: absolute; left: 148px; top: 552px; width: 332px; font-size: 9.6px; line-height: 1.36; font-weight: 600; text-align: justify; }
  .bio-text strong { color: var(--orange); font-weight: 700; }
  /* spine */
  .spine {
    position: absolute; left: 548px; top: 0; width: 64px; height: 100%;
    background: linear-gradient(180deg, #04060b, #0a1018 50%, #04060b);
  }
  .spine__title, .spine__author {
    position: absolute; left: 50%; writing-mode: vertical-rl;
    transform: translateX(-50%);
    font-family: "Saira Condensed", sans-serif; font-weight: 500; text-transform: uppercase;
  }
  .spine__title {
    top: 28px; font-size: 19px; letter-spacing: 3.6px;
    background: linear-gradient(180deg, var(--orange), var(--pink) 50%, var(--blue));
    -webkit-background-clip: text; background-clip: text; color: transparent;
  }
  .spine__author { bottom: 24px; font-size: 18px; letter-spacing: 3px; color: var(--orange); font-weight: 600; }
  /* front cover */
  .front { position: absolute; left: 612px; top: 0; width: 553px; height: 100%; background: var(--ink); }
  .front__art {
    position: absolute; left: 0; top: 0; width: 100%; height: 100%;
    background:
      radial-gradient(ellipse 46% 30% at 50% 62%, rgba(60,110,255,0.75), rgba(60,110,255,0) 70%),
      radial-gradient(ellipse 55% 62% at 48% 55%, rgba(214,72,110,0.85), rgba(150,40,90,0.35) 55%, rgba(5,7,12,0) 80%),
      radial-gradient(ellipse 80% 40% at 50% 100%, rgba(40,90,160,0.45), rgba(5,7,12,0) 70%),
      linear-gradient(180deg, #04060b, #070c16);
  }
  .front__lines { position: absolute; left: 0; top: 0; }
  .title { position: absolute; font-family: "Saira Condensed", sans-serif; font-weight: 600; text-transform: uppercase; line-height: 0.86; white-space: nowrap; }
  .title--hero {
    left: 66px; top: 142px; font-size: 90px; letter-spacing: -1px;
    background: linear-gradient(180deg, var(--orange-light), var(--orange) 60%, #ff6f5a);
    -webkit-background-clip: text; background-clip: text; color: transparent;
  }
  .title--second {
    left: 68px; top: 262px; font-size: 57px;
    background: linear-gradient(180deg, var(--orange-light), var(--orange));
    -webkit-background-clip: text; background-clip: text; color: transparent;
  }
  .title--link { left: 248px; top: 114px; font-size: 40px; color: var(--white); }
  .title--main {
    left: 232px; top: 166px; font-size: 78px; line-height: 0.9;
    background: linear-gradient(90deg, var(--pink), var(--violet) 55%, var(--blue));
    -webkit-background-clip: text; background-clip: text; color: transparent;
  }
  .front__quote {
    position: absolute; left: 40px; top: 362px; width: 473px; text-align: center;
    font-size: 13px; font-weight: 700; line-height: 1.35; color: var(--white);
  }
  .front__credit { display: block; font-weight: 600; font-size: 12.5px; }
  .front__credit b { color: var(--gold); font-weight: 700; }
  .front__author {
    position: absolute; left: 0; width: 100%; top: 700px; text-align: center; white-space: nowrap;
    font-family: "Saira", sans-serif; font-weight: 700; font-size: 44px; letter-spacing: 9px;
    text-transform: uppercase; color: var(--white);
  }
</style>
</head>
<body>
  <main class="spread">
    <section class="back">
      <h2 class="back__heading">Praise for <span>Nine Doors Past the Glowing Screen</span></h2>

      <blockquote class="praise praise--one">“A must-read for anyone who is addicted to or thinks they may have a problem with digital gaming. This eloquent work will also be useful to academics and clinicians exploring potential solutions. The author recognizes the similarities between gaming addiction and other addictions, and logically applies one of the most effective known solutions for addiction - The Twelve Steps.”
        <span class="praise__name"><b>DALE WHITCOMBE,</b> Noted Interventionist and Keynote Speaker</span>
      </blockquote>

      <blockquote class="praise praise--two">“If you suffer from digital gaming addiction, I strongly encourage you to use this book as your road map to get you back to the real world.”
        <span class="praise__name"><b>OWEN PRATLEY,</b> Founder of Feed Signal Weekly.</span>
      </blockquote>

      <blockquote class="praise praise--three">“As a high school teacher for 24 years, husband, father, coach, and 12-Step member, I can assure you that this book will transform the life of anyone who is addicted to video games. Well written, easy to understand, and a wonderful book that will provide you with a clear road map to recovery, and this includes teenagers, a group I have been working with in the classroom for decades.”
        <span class="praise__name"><b>REUBEN SALCEDO, HARBOR VALE,</b> OR High School Teacher.</span>
      </blockquote>

      <div class="divider"></div>

      <div class="blurb">
        <p>A Practical Path Beyond Compulsive Console Play, based on the rich and successful tradition of the Twelve Steps.</p>
        <p>Addiction to Digital Gaming is a new and troubling phenomenon that has burst upon an unprepared society with alarming speed. Many people crave the use of Digital Games in a strikingly similar way to any other addict. Digital Games are a complex software and hardware system that have been designed to promote continued and progressive usage. This sophisticated technology clearly feeds on natural addictive tendencies.</p>
        <p>THE 12 STEPS are one of the most effective methods for treating addiction in human history. Originating with RL in 1939, the 12 Steps have since been used to treat a variety of other addictions, including drugs, sex, gambling, eating disorders, and many others. Now in this groundbreaking work the 12 Steps are applied to the complex and evolving contemporary phenomenon of Digital Gaming Addiction.</p>
      </div>

      <div class="bio-band"></div>
      <div class="bio-photo" role="img" aria-label="Author portrait photograph"></div>
      <p class="bio-text"><strong>MARTIN QUORBY</strong> is a Technology Consultant and Writer with many years of professional coding and consulting experience. He also struggled with addiction to drugs and alcohol and is now clean and sober in a Twelve-Step program for over 17 years. This unique combination of 12-Step experience and technology expertise led him to create Nine Doors Past the Glowing Screen.</p>
    </section>

    <section class="spine">
      <span class="spine__title">Nine Doors Past the Glowing Screen</span>
      <span class="spine__author">Martin Quorby</span>
    </section>

    <section class="front">
      <div class="front__art" role="img" aria-label="Illustration of a hand holding a glowing game controller in pink, red and blue light"></div>
      <svg class="front__lines" width="553" height="792" viewBox="0 0 553 792" aria-hidden="true">
        <g stroke="var(--line)" stroke-width="1.5" fill="none">
          <line x1="68" y1="58" x2="215" y2="58"/>
          <line x1="215" y1="58" x2="215" y2="326"/>
          <line x1="215" y1="92" x2="232" y2="92"/>
          <line x1="215" y1="326" x2="530" y2="326"/>
        </g>
        <circle cx="238" cy="92" r="6" fill="var(--steel)"/>
        <circle cx="215" cy="326" r="4.5" fill="var(--steel)"/>
      </svg>
      <div class="title title--hero">Nine</div>
      <div class="title title--second">Doors</div>
      <div class="title title--link">Past the</div>
      <div class="title title--main">Glowing<br>Screen</div>
      <p class="front__quote">“A must-read for anyone who is addicted to or thinks they may have a problem with digital gaming...”
        <span class="front__credit"><b>DALE WHITCOMBE |</b> Noted Interventionist and Keynote Speaker</span>
      </p>
      <div class="front__author">Martin Quorby</div>
    </section>
  </main>
</body>
</html>
```